Talvon Crest Real estate in need of Logo design

I just started a new real estate brokerage company and need a professional, new logo design that I can incorporate through all forms of marketing and branding. I would like the business card to use both Matte finish and high gloss.

```html
<!DOCTYPE html>
<html lang="en">
<head>
<meta charset="utf-8">
<title>Talvon Crest Real estate – Business Card</title>
<link href="https://fonts.googleapis.com/css2?family=Work+Sans:wght@400;500;600&display=swap" rel="stylesheet">
<style>
  :root {
    --gold: #c8961f;
    --charcoal: #4a4a4c;
    --card-dark: #3c3c3e;
    --card-light: #ffffff;
    --text-grey: #3a3a3a;
    --soft-grey: #cfcfcf;
    --backdrop: #e4e4e6;
  }
  * { margin: 0; padding: 0; box-sizing: border-box; }
  html, body {
    width: 1200px;
    height: 900px;
    overflow: hidden;
    background: var(--backdrop);
    font-family: "Work Sans", Arial, sans-serif;
  }
  .canvas {
    width: 1200px;
    height: 900px;
    display: flex;
    flex-direction: column;
    align-items: center;
    justify-content: center;
    gap: 40px;
  }
  .card {
    width: 560px;
    height: 320px;
    border-radius: 22px;
    position: relative;
    box-shadow: 0 10px 28px rgba(0,0,0,0.18);
  }
  .card--front { background: var(--card-light); }
  .card--back { background: var(--card-dark); }

  .brand {
    position: absolute;
    display: flex;
    align-items: center;
    gap: 12px;
    font-weight: 600;
    text-transform: uppercase;
  }
  .brand__square {
    width: 14px;
    height: 14px;
    background: var(--gold);
    flex: none;
  }
  .card--front .brand {
    left: 46px;
    top: 58px;
    font-size: 19px;
    letter-spacing: 0.12em;
    color: var(--gold);
  }
  .card--back .brand {
    left: 50%;
    top: 50%;
    transform: translate(-50%, -50%);
    font-size: 26px;
    letter-spacing: 0.14em;
    color: var(--soft-grey);
    white-space: nowrap;
  }
  .card--back .brand__square { width: 18px; height: 18px; }

  .contact {
    position: absolute;
    left: 290px;
    top: 128px;
    color: var(--text-grey);
    font-size: 15px;
    line-height: 1.45;
  }
  .contact__name {
    color: var(--gold);
    font-weight: 500;
    font-size: 21px;
    letter-spacing: 0.12em;
    text-transform: uppercase;
  }
  .contact__role { font-size: 14px; margin-bottom: 10px; }
  .contact__address { margin-bottom: 10px; }
  .contact__line {
    display: flex;
    align-items: center;
    gap: 8px;
  }
  .contact__line svg { width: 11px; height: 11px; flex: none; }
  .contact__domain { color: var(--gold); }
</style>
</head>
<body>
<main class="canvas">
  <section class="card card--front" aria-label="Business card front">
    <div class="brand"><span class="brand__square"></span>Talvon Crest Real estate</div>
    <div class="contact">
      <p class="contact__name">Dorian Hale</p>
      <p class="contact__role">Director</p>
      <p class="contact__address">214b Fenwick Lane,<br>Ashford, NZ, 7020</p>
      <p class="contact__line">
        <svg viewBox="0 0 12 12" aria-hidden="true"><path d="M2.5 1 L4.5 1 L5.2 3.6 L3.9 4.6 C4.6 6 5.9 7.3 7.3 8 L8.3 6.7 L11 7.4 L11 9.5 C11 10.3 10.3 11 9.5 11 C5 10.6 1.4 7 1 2.5 C1 1.7 1.7 1 2.5 1 Z" fill="var(--gold)"/></svg>
        (555) 013-4782
      </p>
      <p class="contact__line">
        <svg viewBox="0 0 12 12" aria-hidden="true"><rect x="1" y="2.5" width="10" height="7" rx="1" fill="none" stroke="var(--gold)" stroke-width="1.3"/><path d="M1.5 3 L6 6.5 L10.5 3" fill="none" stroke="var(--gold)" stroke-width="1.3"/></svg>
        info@talvoncrest.com
      </p>
      <p class="contact__line">
        <svg viewBox="0 0 12 12" aria-hidden="true"><circle cx="6" cy="6" r="5" fill="none" stroke="var(--gold)" stroke-width="1.2"/><ellipse cx="6" cy="6" rx="2.2" ry="5" fill="none" stroke="var(--gold)" stroke-width="1"/><path d="M1 6 H11" stroke="var(--gold)" stroke-width="1"/></svg>
        <span>www.<span class="contact__domain">talvoncrest</span>.com</span>
      </p>
    </div>
  </section>

  <section class="card card--back" aria-label="Business card back">
    <div class="brand"><span class="brand__square"></span>Talvon Crest Real estate</div>
  </section>
</main>
</body>
</html>
```